Web Header needed for an inspirational coaching company's website - ongoing work

We need a beautifully designed web header to replace my current one at my homepage on my website www.kelvoria.com
There will be continuous work required for various creative work in the future if your work is selected.
I work with corporate professionals and executives to bring clarity and joy back to their career. It needs to be elegant, sophisticated, intelligent, but friendly and inspiring at the same time.
Thank you!
Target Market(s)
Corporate profesionals and executives
Industry/Entity Type
It Company
Colors
Designer to choose colors to be used in the design.
Look and feel

```html
<!DOCTYPE html>
<html lang="en">
<head>
<meta charset="utf-8">
<title>Kelvoria – Bring Clarity to Your Career</title>
<link rel="stylesheet" href="https://fonts.googleapis.com/css2?family=Great+Vibes&display=swap">
<style>
  :root {
    --teal-light: #45dcc6;
    --teal-mid: #27b79d;
    --teal-deep: #138a72;
    --headline: #ffffff;
    --headline-shadow: rgba(10, 50, 42, 0.8);
    --photo-dark: #2a2220;
    --photo-warm: #b8573a;
  }
  html, body {
    margin: 0;
    padding: 0;
    overflow: hidden;
  }
  .site-header {
    position: relative;
    width: 1200px;
    height: 539px;
    overflow: hidden;
    background:
      radial-gradient(ellipse 70% 80% at 78% 12%, var(--teal-light) 0%, rgba(69,220,198,0) 70%),
      radial-gradient(ellipse 60% 90% at 0% 70%, var(--teal-deep) 0%, rgba(19,138,114,0) 75%),
      linear-gradient(180deg, var(--teal-mid) 0%, #1fa589 100%);
  }
  .coach-portrait {
    position: absolute;
    left: 188px;
    top: 152px;
    width: 292px;
    height: 387px;
    background: linear-gradient(180deg, var(--photo-dark) 0%, var(--photo-dark) 45%, var(--photo-warm) 100%);
    box-shadow: 0 0 18px rgba(255, 255, 255, 0.2);
  }
  .headline {
    position: absolute;
    left: 608px;
    top: 252px;
    margin: 0;
    font-family: "Great Vibes", cursive;
    font-weight: 400;
    font-size: 80px;
    line-height: 104px;
    color: var(--headline);
    -webkit-text-stroke: 1px var(--headline);
    text-shadow: 2px 3px 4px var(--headline-shadow);
    white-space: nowrap;
  }
  .headline-line {
    display: block;
  }
</style>
</head>
<body>
  <header class="site-header">
    <div class="coach-portrait" role="img" aria-label="Portrait photograph of the coach"></div>
    <h1 class="headline">
      <span class="headline-line">Bring Clarity</span>
      <span class="headline-line">to Your Career</span>
    </h1>
  </header>
</body>
</html>
```